Modern Design Business Card industrial maintenance company

Business card design for Company named Brookvale Equipment Services

Target Market(s)

Industrial

Industry/Entity Type

Maintenance and repair

Contact Information for Business Card

Place holder for address, office phone, mobile number and email

Requirements
Must have
• Clean modern look
Nice to have
• N/a

```html
<!DOCTYPE html>
<html lang="en">
<head>
<meta charset="UTF-8">
<title>Brookvale Equipment Services — Business Card</title>
<link rel="stylesheet" href="https://fonts.googleapis.com/css2?family=Montserrat:wght@500;600;800&display=swap">
<style>
  :root {
    --backdrop: #f7c499;
    --ink: #000000;
    --paper: #ffffff;
    --paper-shade: #f2f2f2;
  }
  * { margin: 0; padding: 0; box-sizing: border-box; }
  html, body {
    width: 1200px; height: 800px; overflow: hidden;
    background: var(--backdrop);
    font-family: "Montserrat", Arial, sans-serif;
  }
  .stage {
    position: relative; width: 1200px; height: 800px;
    display: flex; align-items: center; justify-content: center; gap: 40px;
  }
  .card {
    position: relative; width: 540px; height: 309px;
    background: linear-gradient(135deg, var(--paper), var(--paper-shade));
    overflow: hidden;
    box-shadow: 0 18px 40px rgba(0,0,0,0.12);
  }

  /* Front */
  .holder { position: absolute; left: 30px; top: 52px; color: var(--ink); }
  .holder-name { font-weight: 800; font-size: 32px; letter-spacing: 0.5px; line-height: 1.1; }
  .holder-role { font-weight: 500; font-size: 22px; letter-spacing: 4px; margin-top: 4px; }

  .brand {
    position: absolute; right: 26px; top: 28px; width: 200px;
    display: flex; flex-direction: column; align-items: center; gap: 10px;
  }
  .brand-dot { width: 62px; height: 62px; border: 4px solid var(--ink); border-radius: 50%; }
  .brand-name {
    font-weight: 600; font-size: 14px; letter-spacing: 2px; line-height: 1.35;
    color: var(--ink); text-align: center; text-transform: uppercase;
  }

  .band { position: absolute; left: 0; right: 0; background: var(--ink); display: flex; align-items: center; }
  .band-upper { top: 188px; height: 36px; }
  .band-lower { top: 232px; bottom: 0; }
  .contact-row { display: flex; align-items: center; width: 100%; padding-left: 118px; padding-right: 24px; justify-content: space-between; }
  .contact {
    display: flex; align-items: center; gap: 10px;
    color: var(--paper); font-weight: 800; font-size: 14px; letter-spacing: 0.8px;
  }
  .contact-icon {
    width: 24px; height: 24px; border-radius: 50%; background: var(--paper);
    display: flex; align-items: center; justify-content: center;
  }
  .contact-icon svg { width: 14px; height: 14px; }

  .badge {
    position: absolute; left: 4px; top: 184px; width: 96px; height: 96px;
    border-radius: 50%; background: var(--paper);
    border: 5px solid var(--ink); box-shadow: 0 0 0 4px var(--paper);
  }

  /* Back */
  .back-art { position: absolute; inset: 0; }
  .back-brand {
    position: absolute; left: 140px; top: 70px; width: 360px;
    display: flex; align-items: center; gap: 16px;
  }
  .back-brand .brand-dot { width: 74px; height: 74px; flex: none; }
  .back-brand .brand-name { text-align: left; font-size: 17px; }
</style>
</head>
<body>
<main class="stage">

  <section class="card card-front" aria-label="Business card front">
    <div class="holder">
      <p class="holder-name">YOUR NAME</p>
      <p class="holder-role">JOB POSITION</p>
    </div>

    <div class="brand">
      <span class="brand-dot"></span>
      <p class="brand-name">Brookvale<br>Equipment Services</p>
    </div>

    <div class="band band-upper">
      <div class="contact-row">
        <span class="contact">
          <span class="contact-icon">
            <svg viewBox="0 0 16 16" fill="none" stroke="#000" stroke-width="1.5"><rect x="2" y="4" width="12" height="9"/><path d="M2 4l6 5 6-5"/></svg>
          </span>WWW.YOUREMAIL.COM
        </span>
        <span class="contact">
          <span class="contact-icon">
            <svg viewBox="0 0 16 16" fill="none" stroke="#000" stroke-width="1.5"><path d="M2 6c0-2 2-3 6-3s6 1 6 3v1h-3V6H5v1H2z"/><rect x="4" y="8" width="8" height="5"/><circle cx="8" cy="10.5" r="1.2"/></svg>
          </span>123-4567-890
        </span>
      </div>
    </div>

    <div class="band band-lower">
      <div class="contact-row">
        <span class="contact">
          <span class="contact-icon">
            <svg viewBox="0 0 16 16" fill="none" stroke="#000" stroke-width="1.5"><path d="M4 2l2 3-1.5 1.5a8 8 0 0 0 5 5L11 10l3 2-1 2c-6 0-11-5-11-11z"/></svg>
          </span>123-4567-890
        </span>
        <span class="contact">
          <span class="contact-icon">
            <svg viewBox="0 0 16 16" fill="none" stroke="#000" stroke-width="1.5"><path d="M8 15s5-5 5-9a5 5 0 0 0-10 0c0 4 5 9 5 9z"/><circle cx="8" cy="6" r="1.8"/></svg>
          </span>YOUR ADDRESS
        </span>
      </div>
    </div>

    <span class="badge"></span>
  </section>

  <section class="card card-back" aria-label="Business card back">
    <svg class="back-art" viewBox="0 0 540 309" aria-hidden="true">
      <rect x="0" y="0" width="42" height="309" fill="#000"/>
      <rect x="0" y="269" width="540" height="40" fill="#000"/>
      <rect x="52" y="0" width="30" height="259" fill="#000"/>
      <rect x="52" y="229" width="488" height="30" fill="#000"/>
      <circle cx="66" cy="244" r="50" fill="#fff"/>
      <circle cx="66" cy="244" r="42" fill="#fff" stroke="#000" stroke-width="5"/>
    </svg>
    <div class="back-brand">
      <span class="brand-dot"></span>
      <p class="brand-name">Brookvale<br>Equipment Services</p>
    </div>
  </section>

</main>
</body>
</html>
```